Business Card Design

I am a mental health counselor in private practice. I provide counseling to individuals, couples, and adults. There is a design on CardLoom that I really like. It is 2 talking bubbles joined together by a heart. That is just a suggestion. I'm interested in other ideas. I would like my photo to be on the back of the card, along with the text Miriam Delacott Counseling. I would like mint green as my background color and navy writing, if possible. The final design should be elegant, professional, and maybe just a touch whimsical.
Target Market(s)
Individual adolescents, adults, couples, and families seeking counseling.
Industry/Entity Type
Mental Health
Contact Information for Business Card
Miriam Delacott
A Wholehearted Approach to Counseling
Miriam Delacott, M.S. NCC
Wexmoor Hall
2947 NW Calloway Street, Suite 318
Portland OR 97209
503-286-1573
counselingwithmiriam-example.com
Requirements
Must have
- The card must have all of the text provided and my photo.
Nice to have
- I like cards that are rounded on the sides, and I like thick paper.

```html
<!DOCTYPE html>
<html lang="en">
<head>
<meta charset="utf-8">
<title>Miriam Delacott Counseling – Business Card</title>
<link rel="stylesheet" href="https://fonts.googleapis.com/css2?family=Caveat:wght@400&family=Marcellus+SC&family=Mulish:ital,wght@1,400&display=swap">
<style>
  :root {
    --mint: #a2f682;
    --mint-soft: #b8f89c;
    --white: #ffffff;
    --navy: #1b2a7a;
    --mark-pale: #d6f8b8;
    --mark-lime: #a6f26a;
    --photo-tone: #c9c2b6;
  }
  * { margin: 0; padding: 0; box-sizing: border-box; }
  html, body { width: 1000px; height: 1200px; overflow: hidden; background: var(--white); }
  .sheet { position: relative; width: 1000px; height: 1200px; }

  .band { position: absolute; left: 0; width: 1000px; background: var(--mint); }
  .band--top { top: 0; height: 75px; }
  .band--bottom { top: 1120px; height: 80px; }

  .card-front {
    position: absolute; top: 75px; left: 0; width: 1000px; height: 525px;
    background: linear-gradient(to bottom, var(--white) 0%, #e6fcd9 45%, var(--mint-soft) 100%);
  }
  .card-back {
    position: absolute; top: 603px; left: 0; width: 1000px; height: 517px;
    background: linear-gradient(to bottom, var(--mint-soft) 0%, #e9fcdf 45%, var(--white) 75%);
  }

  .info-frame {
    position: absolute; left: 49px; top: 0; width: 905px; height: 448px;
    border: 3px solid var(--white); border-top: none;
  }

  .emblem-area {
    position: absolute; left: 710px; top: 68px; width: 174px; height: 88px;
    border-radius: 44px;
    background: linear-gradient(90deg, var(--mark-pale) 0%, var(--mark-lime) 100%);
  }

  .name {
    position: absolute; left: 106px; top: 126px;
    font-family: "Caveat", cursive; font-weight: 400; font-size: 66px; color: var(--navy);
    line-height: 1; white-space: nowrap;
  }
  .details {
    position: absolute; left: 97px; top: 206px;
    font-family: "Marcellus SC", serif; font-size: 27px; color: var(--navy);
    line-height: 46px; white-space: nowrap; letter-spacing: 0.6px;
  }
  .details .web {
    font-family: "Mulish", sans-serif; font-style: italic; font-size: 25px; letter-spacing: 0;
  }

  .photo {
    position: absolute; left: 550px; top: 167px; width: 352px; height: 297px;
    border: 7px solid var(--mint);
    background: linear-gradient(160deg, #eeeeec 0%, var(--photo-tone) 55%, #6d665e 100%);
  }
  .practice-name {
    position: absolute; left: 95px; top: 418px;
    font-family: "Caveat", cursive; font-weight: 400; font-size: 46px; color: var(--navy);
    white-space: nowrap; line-height: 1;
  }
</style>
</head>
<body>
<main class="sheet">
  <div class="band band--top"></div>

  <section class="card-front">
    <div class="info-frame"></div>
    <div class="emblem-area" role="img" aria-label="Decorative emblem area of overlapping hearts in pale green, lime and red"></div>
    <h1 class="name">Miriam Delacott</h1>
    <p class="details">
      A Wholehearted Approach to Counseling Miriam Delacott<br>
      M.S. NCC Wexmoor Hall 2947 NW Calloway Street<br>
      Suite 318 Portland OR 97209 503-286-1573<br>
      <span class="web">counselingwithmiriam-example.com</span>
    </p>
  </section>

  <section class="card-back">
    <div class="photo" role="img" aria-label="Portrait photo of the counselor in front of a bookshelf"></div>
    <p class="practice-name">Miriam Delacott Counseling</p>
  </section>

  <div class="band band--bottom"></div>
</main>
</body>
</html>
```